We need an attractive business card design that is modern and inviting. We like the blue and yellow (or gold) colors that are displayed with the logo. The business should communicate trust, experience, and integrity.

Target Market(s)

Residential and Commercial

Industry/Entity Type

Business

Contact Information for Business Card

Recessed Lighting
LED Retro Fit
Sign Repair
Alarms and Cameras
Mobile Home Services
24hr service calls

Font styles to use
Serif
Sans Serif

Colors
3176b5
0455a3
fece3e
fbee3e

Requirements
Must have
• Brondle Electric
• Owner: Marcus Tivane
• Licensed and Insured
• TECL #58917
Nice to have
• Exquisite Detail!!
• Over 20 years of experience
Should not have
• Nothing boring or traditional!!!

```html
<!DOCTYPE html>
<html lang="en">
<head>
<meta charset="utf-8">
<title>Brondle Electric – Business Card</title>
<link href="https://fonts.googleapis.com/css2?family=Open+Sans:wght@400;600;700&display=swap" rel="stylesheet">
<style>
  :root {
    --blue: #0d4f9c;
    --blue-deep: #0a4790;
    --blue-mark: #0b3f82;
    --yellow: #f2e531;
    --ink: #2b2b2b;
    --muted: #555;
    --rule: #7a7a7a;
    --ghost: #efefef;
    --stage: #e4e4e7;
    --white: #ffffff;
  }
  * { margin: 0; padding: 0; box-sizing: border-box; }
  html, body { width: 1200px; height: 720px; overflow: hidden; }
  body {
    background: var(--stage);
    font-family: "Open Sans", Arial, sans-serif;
    position: relative;
  }
  .card {
    position: absolute;
    top: 223px;
    width: 465px;
    height: 266px;
    overflow: hidden;
  }
  .card--front { left: 125px; background: var(--white); }
  .card--back { left: 610px; background: var(--blue-deep); }

  .ghost-ring { position: absolute; left: 0; top: 0; }

  .brand-dot {
    position: absolute;
    border-radius: 50%;
  }
  .card--front .brand-dot {
    left: 89px; top: 22px; width: 57px; height: 57px;
    border: 4px solid var(--blue);
  }
  .brand-name {
    position: absolute;
    font-weight: 600;
    letter-spacing: 0.5px;
    white-space: nowrap;
  }
  .card--front .brand-name {
    left: 22px; top: 81px;
    font-size: 20px;
    color: var(--blue);
  }

  .owner {
    position: absolute;
    right: 22px; top: 133px;
    text-align: right;
  }
  .owner__name {
    font-size: 16px; font-weight: 700; color: var(--blue);
    letter-spacing: 0.3px; line-height: 18px;
  }
  .owner__title {
    font-size: 12px; color: var(--muted); line-height: 15px;
  }
  .divider {
    position: absolute;
    left: 22px; top: 158px;
    width: 302px; height: 1px;
    background: var(--rule);
  }
  .services {
    position: absolute;
    left: 22px; top: 164px;
    list-style: none;
    font-size: 11.5px; line-height: 15px;
    color: var(--ink);
  }
  .services .dot { color: var(--blue); font-size: 9px; vertical-align: 1px; margin-right: 2px; }

  .contact {
    position: absolute;
    right: 22px; top: 173px;
    list-style: none;
    text-align: right;
    font-size: 11.5px; line-height: 15.3px;
    color: var(--ink);
  }
  .contact li { display: flex; justify-content: flex-end; align-items: center; gap: 5px; }
  .contact svg { width: 10px; height: 10px; fill: var(--blue); }

  .band { position: absolute; bottom: 0; height: 13px; }
  .band--blue { left: 0; width: 230px; background: var(--blue); }
  .band--yellow { left: 234px; right: 0; background: var(--yellow); }

  .card--back .brand-dot {
    left: 306px; top: 71px; width: 64px; height: 64px;
    border: 4px solid var(--white);
  }
  .card--back .brand-name {
    left: 0; width: 674px; text-align: center; top: 138px;
    font-size: 23px; color: var(--white);
  }
  .tagline {
    position: absolute;
    left: 0; width: 674px; top: 168px;
    text-align: center;
    font-size: 13.5px; color: var(--white);
  }
</style>
</head>
<body>

<section class="card card--front" aria-label="Front of business card">
  <svg class="ghost-ring" width="465" height="266" aria-hidden="true">
    <circle cx="435" cy="129" r="100" fill="none" stroke="var(--ghost)" stroke-width="20"/>
  </svg>

  <span class="brand-dot" aria-hidden="true"></span>
  <div class="brand-name">BRONDLE ELECTRIC</div>

  <div class="owner">
    <div class="owner__name">MARCUS TIVANE</div>
    <div class="owner__title">Licensed and Insured</div>
  </div>
  <div class="divider"></div>

  <ul class="services">
    <li><span class="dot">●</span>24hr service calls</li>
    <li><span class="dot">●</span>Residential &amp; Commercial</li>
    <li><span class="dot">●</span>Recessed Lighting <span class="dot">●</span>LED Retro Fit</li>
    <li><span class="dot">●</span>Sign Repair <span class="dot">●</span>Alarms and Cameras</li>
    <li><span class="dot">●</span>Mobile Home Services</li>
  </ul>

  <ul class="contact">
    <li>+ 000 000 0000
      <svg viewBox="0 0 10 10" aria-label="Phone"><path d="M1 4 Q5 0 9 4 L8 5 L7 4 L3 4 L2 5 Z M3 5 L7 5 L8 9 L2 9 Z"/></svg></li>
    <li>+ 000 000 0000
      <svg viewBox="0 0 10 10" aria-label="Fax"><rect x="3" y="1" width="4" height="3"/><rect x="1" y="4" width="8" height="3.5"/><rect x="3" y="7" width="4" height="2.5"/></svg></li>
    <li>Info@BrondleElectric.com
      <svg viewBox="0 0 10 10" aria-label="Email"><path d="M1 2 H9 V8 H1 Z" /><path d="M1 2 L5 5.5 L9 2" stroke="#fff" stroke-width="0.9" fill="none"/></svg></li>
    <li>www.BrondleElectric.com
      <svg viewBox="0 0 10 10" aria-label="Website"><circle cx="5" cy="5" r="4" fill="none" stroke="var(--blue)" stroke-width="1.3"/><path d="M5 5 L9.5 7 L7.5 7.5 L7 9.5 Z"/></svg></li>
  </ul>

  <div class="band band--blue"></div>
  <div class="band band--yellow"></div>
</section>

<section class="card card--back" aria-label="Back of business card">
  <svg class="ghost-ring" width="465" height="266" aria-hidden="true">
    <circle cx="30" cy="133" r="105" fill="none" stroke="var(--blue-mark)" stroke-width="17"/>
  </svg>
  <span class="brand-dot" aria-hidden="true" style="left:238px;top:71px"></span>
  <div class="brand-name" style="left:0;width:541px">BRONDLE ELECTRIC</div>
  <div class="tagline" style="width:541px">Over 20 years of experience</div>
</section>

</body>
</html>
```